Business Identity Stationary

Already have the logo which is in the attached files so only need the Business STationary
1) Double Sided Business Card
2) Letterhead
3) Presentation folder with business card holder on inside cover
4) WIth compliments slip
See information for business cards, letterhead and presentation folder below.

This should be a simply job using a logo we already had designed along with a little device. I suggest using the device off center and perhaps lower in the corner in an abstract way. Also the logo device could be used as a watermark for the letterhead. The designer who created the logo presented something that I think works well for a business card. The front of the double sided business card could have the name logo small for the website address and only use the Lime device on the front. Then on the back could be the name Parvel Advisory logo.

Please note that for the business card the black and lime green background do look good. Also please think of using the lime device separately in an unusual way.

It has been brought to my attention that.my budget was far to low. Hopefully this.will attract you to the project. 

The parent company of Parvel Advisory is BrightHeron holdings. I have uploaded a file of the Bright Heron business card I really like. Perhaps use this business card as a guide to the type of modern and clean style I am looking for. It also works to have the Parvel Advisroy and Bright Heron similar.

Industry/Entity Type

Business

Font styles to use
Sans Serif

Colors
9bcb3c
000000
5c5c5c
add136
cadf82
eaf2cf
f9fbf2
1b1b1b
757575

Requirements
Must have
• 1) Double Sided Business Card
Renata Tolberg
Director
Tel: +505 8426 3057
Email: rtb@parveladvisory.com
Website: www.parveladvisory.com

Gregory Tolberg
Director
Tel: +505 8426 3092
Email: gkb@parveladvisory.com

Helena Pardo Duvignac
Director
Tel: 8342 1168
Email: hpd@parveladvisory.com

2) Letterhead
Logo
Lime Logo Device
Website Address: www.parveladvisory.com
Small print on bottom: Parvel Advisory a Bright Heron Holding Company SA. RUC K0470000283914

3) Presentation Folder
Traditional Presentation folder with inside front cover spot for the insertion of business card.

4) With Compliments slip

```html
<!DOCTYPE html>
<html lang="en">
<head>
<meta charset="utf-8">
<title>Parvel Advisory — Business Card</title>
<link href="https://fonts.googleapis.com/css2?family=Montserrat:wght@400;500;600;700&family=Open+Sans:wght@400;600&display=swap" rel="stylesheet">
<style>
  :root {
    --lime: #9bcb3c;
    --lime-bright: #add136;
    --lime-pale: #cadf82;
    --black: #000000;
    --ink: #1b1b1b;
    --grey: #5c5c5c;
    --grey-light: #757575;
    --paper: #ffffff;
    --backdrop: #eef0ea;
  }
  * { margin: 0; padding: 0; box-sizing: border-box; }
  html, body { width: 1200px; height: 1024px; overflow: hidden; }
  body {
    background: var(--backdrop);
    font-family: "Open Sans", Arial, sans-serif;
    position: relative;
  }

  /* ---------- Front card ---------- */
  .card-front {
    position: absolute;
    left: 50px; top: 318px;
    width: 680px; height: 388px;
    background: var(--paper);
    overflow: hidden;
    box-shadow: 0 6px 18px rgba(0,0,0,.18);
  }
  .card-front .swoosh { position: absolute; inset: 0; }
  .brand {
    position: absolute;
    display: flex; align-items: center; gap: 12px;
    font-family: "Montserrat", Arial, sans-serif;
    font-weight: 600;
    white-space: nowrap;
  }
  .card-front .brand {
    left: 52px; top: 112px;
    font-size: 34px;
    color: var(--black);
  }
  .brand-dot {
    width: 22px; height: 22px;
    border-radius: 50%;
    background: var(--lime);
    flex: none;
  }
  .divider {
    position: absolute;
    left: 418px; top: 70px;
    width: 1px; height: 110px;
    background: var(--grey-light);
  }
  .contact-list {
    position: absolute;
    left: 438px; top: 70px;
    list-style: none;
    font-size: 13px;
    color: var(--grey);
    line-height: 24px;
  }
  .contact-list li { display: flex; align-items: center; gap: 8px; }
  .contact-list svg { width: 13px; height: 13px; flex: none; }
  .holder {
    position: absolute;
    left: 52px; top: 282px;
    font-family: "Montserrat", Arial, sans-serif;
  }
  .holder-name {
    color: var(--lime);
    font-weight: 700;
    font-size: 17px;
  }
  .holder-role {
    color: var(--grey);
    font-size: 13px;
    font-weight: 500;
  }

  /* ---------- Back card ---------- */
  .card-back {
    position: absolute;
    left: 780px; top: 172px;
    width: 370px; height: 648px;
    background: var(--ink);
    overflow: hidden;
    box-shadow: 0 6px 18px rgba(0,0,0,.25);
  }
  .card-back-face {
    position: absolute;
    left: 50%; top: 50%;
    width: 648px; height: 370px;
    transform: translate(-50%, -50%) rotate(90deg);
  }
  .back-disc {
    position: absolute;
    left: 310px; top: 100px;
    width: 170px; height: 170px;
    border-radius: 50%;
    background: #2f3a1c;
  }
  .card-back .brand {
    left: 130px; top: 160px;
    font-size: 46px;
    color: var(--paper);
  }
  .back-web {
    position: absolute;
    left: 170px; top: 290px;
    font-family: "Montserrat", Arial, sans-serif;
    font-size: 15px;
    font-weight: 500;
    color: var(--paper);
    letter-spacing: .3px;
  }
  .back-web .domain { color: var(--lime); }
</style>
</head>
<body>

<section class="card-front" aria-label="Business card, front">
  <svg class="swoosh" viewBox="0 0 680 388" preserveAspectRatio="none" aria-hidden="true">
    <path d="M0,388 L0,372 C250,366 520,318 680,118 L680,388 Z" fill="var(--lime)"/>
    <path d="M40,368 C300,356 540,300 668,110 C580,280 330,352 40,368 Z" fill="var(--black)"/>
  </svg>

  <div class="brand"><span class="brand-dot"></span>Parvel Advisory</div>

  <div class="divider"></div>

  <ul class="contact-list">
    <li>
      <svg viewBox="0 0 16 16"><path fill="var(--lime)" d="M3.6 1.5l2.2 2.6-1.2 1.6c.9 2 2.4 3.5 4.4 4.4l1.6-1.2 2.6 2.2-1.3 2.2C6.9 14.6 1.4 9.1 1.4 2.8z"/></svg>
      +505 8426 3057
    </li>
    <li>
      <svg viewBox="0 0 16 16"><rect x="1" y="3" width="14" height="10" fill="var(--lime)"/><path d="M1.5 3.5L8 9l6.5-5.5" stroke="#fff" stroke-width="1.3" fill="none"/></svg>
      rtb@parveladvisory.com
    </li>
    <li>
      <svg viewBox="0 0 16 16"><circle cx="8" cy="8" r="7" fill="var(--lime)"/><path d="M1 8h14M8 1c-3 3.5-3 10.5 0 14M8 1c3 3.5 3 10.5 0 14" stroke="#fff" stroke-width="1" fill="none"/></svg>
      www.parveladvisory.com
    </li>
  </ul>

  <div class="holder">
    <p class="holder-name">Renata Tolberg</p>
    <p class="holder-role">Director</p>
  </div>
</section>

<section class="card-back" aria-label="Business card, back">
  <div class="card-back-face">
    <div class="back-disc"></div>
    <div class="brand">Parvel Advisory</div>
    <p class="back-web">www.<span class="domain">parveladvisory</span>.com</p>
  </div>
</section>

</body>
</html>
```